Quarrel Ridge Advisory Business Card

Quarrel Ridge Advisory is a company that provides consulting services to the Mining Industry.

Whilst Quarrel Ridge Advisory is an Australian based company its client base is the global mining industry.

The essence of Quarrel Ridge Advisory is its a can do organisation that can make a difference to its clients by providing quality assistance and form lasting relationships.
Updates

Target Market(s)

The global Mining Industry.

Industry/Entity Type

Mining

Font styles to use
Serif

Colors

Designer to choose colors to be used in the design.

Requirements
Nice to have
• My thinking is the card would look good in black given the logo.

I would like to see written on the back side of the card " Providing Metallurgical, Management and Corporate Services to the Mining Industry"

```html
<!DOCTYPE html>
<html lang="en">
<head>
<meta charset="utf-8">
<title>Quarrel Ridge Advisory – Business Card</title>
<link rel="stylesheet" href="https://fonts.googleapis.com/css2?family=Source+Serif+4:wght@400;700&display=swap">
<style>
  :root {
    --page-bg: #d9d9db;
    --card-sky: #1b1d21;
    --card-ground: #2b2721;
    --card-ground-deep: #201d19;
    --accent-orange: #f0a023;
    --mark-grey: #5a5a5f;
    --text-light: #e9e9ea;
    --text-muted: #c9cacc;
    --shadow: rgba(0, 0, 0, 0.45);
  }
  * { box-sizing: border-box; margin: 0; padding: 0; }
  html, body {
    width: 1200px;
    height: 1200px;
    overflow: hidden;
  }
  body {
    position: relative;
    background: var(--page-bg);
    font-family: "Source Serif 4", Georgia, serif;
  }
  .card {
    position: absolute;
    overflow: hidden;
    box-shadow: 0 6px 14px var(--shadow);
  }
  .card-photo {
    position: absolute;
    inset: 0;
    background: linear-gradient(180deg, var(--card-sky) 0%, var(--card-ground) 28%, var(--card-ground) 70%, var(--card-ground-deep) 100%);
  }
  .card-front {
    left: 95px;
    top: 180px;
    width: 975px;
    height: 480px;
  }
  .card-back {
    left: 225px;
    top: 622px;
    width: 935px;
    height: 510px;
  }
  .brand-name {
    position: absolute;
    left: 110px;
    top: 130px;
    display: flex;
    align-items: center;
    gap: 14px;
    color: var(--accent-orange);
    font-weight: 700;
    font-size: 42px;
    line-height: 1.08;
  }
  .brand-mark {
    width: 22px;
    height: 22px;
    background: var(--accent-orange);
    flex: none;
  }
  .contact {
    position: absolute;
    right: 95px;
    top: 118px;
    text-align: right;
    word-spacing: 5px;
  }
  .contact-name {
    color: var(--accent-orange);
    font-weight: 700;
    font-size: 30px;
  }
  .contact-role {
    margin-top: 6px;
    color: var(--text-light);
    font-size: 27px;
  }
  .contact-phone {
    margin-top: 44px;
    color: var(--text-light);
    font-size: 29px;
  }
  .contact-email {
    margin-top: 6px;
    color: var(--text-light);
    font-size: 27px;
    word-spacing: 0;
  }
  .website {
    position: absolute;
    left: 350px;
    top: 396px;
    color: var(--text-muted);
    font-weight: 700;
    font-size: 25px;
    letter-spacing: 4px;
  }
  .back-brand {
    position: absolute;
    left: 0;
    right: 0;
    top: 120px;
    text-align: center;
    color: var(--mark-grey);
    font-weight: 700;
    font-size: 72px;
    line-height: 1.1;
  }
  .services-line {
    position: absolute;
    left: 0;
    right: 0;
    top: 370px;
    text-align: center;
    color: var(--accent-orange);
    font-size: 34px;
    line-height: 1.38;
    word-spacing: 9px;
  }
</style>
</head>
<body>
  <section class="card card-front" aria-label="Card front">
    <div class="card-photo" role="img" aria-label="Dark night photograph of a terraced open-pit mine beneath hills"></div>
    <div class="brand-name"><span class="brand-mark"></span><span>Quarrel Ridge<br>Advisory</span></div>
    <div class="contact">
      <p class="contact-name">Dana Whitlow</p>
      <p class="contact-role">Project Manager</p>
      <p class="contact-phone">+61 7 5550 1234</p>
      <p class="contact-email">dwhitlow@quarrelridge.com</p>
    </div>
    <p class="website">quarrelridge.com</p>
  </section>

  <section class="card card-back" aria-label="Card back">
    <div class="card-photo" role="img" aria-label="Dark night photograph of a terraced open-pit mine beneath hills"></div>
    <p class="back-brand">Quarrel Ridge<br>Advisory</p>
    <p class="services-line">Providing Metallurgical, Management and<br>Corporate Services to the Mining Industry</p>
  </section>
</body>
</html>
```